依頼詳細
・企業サイトですが、かたくならず、面白さがほしいです。
・コンテンツ内容は「ごあいさつ」「会社案内」「製品案内」「採用情報」「お問い合わせ」となる予定です。
・TOPページにはスライドショーもしくはそれに変わるものを最初に配置して下さい。
・TOPページと、下層ページのデザインをお願いします。
・TOPページにはNEWS(お知らせ)欄が入る予定です。
・最終的に当方でWordPressにて構築します。
・既存サイトのイメージにとらわれない自由なデザインでもOKです。
ぜひ様々なアイデアをご提案下さい。
サイトURL
http://www.kenro-gear.jp/
ページ数
2ページ
希望イメージ
• +5 0 +5
• シンプル
複雑
• 単色
カラフル
• 暗い
明るい
• 日常
高級
• 遊び心
厳粛
• 未来的
伝統的
• 女性的
男性的
希望する色
青系、グレー系、カラーリングは、添付のロゴマークにある色をベースに考えて頂くと望ましいです。
納品ファイル
• 高解像度JPG (.jpg)
• イラストレーター形式 (.ai)
• フォトショップ形式 (.psd)
補足説明
素材画像で購入が必要なものがある場合、「Pixaveno Media (https://media.pixaveno.com/jp/)」より選定下さい。当方で購入しますので、ご提案の際はカンプ画像を利用いただき、採用後には素材のURL or ファイル番号をお伝えいただきます。

その他ご不明な点がございましたら、お気軽にご連絡下さい。
依頼公開後の追記内容
皆様短い期間の中大変多くの提案をいただきまことにありがとうございました。
ただいま、先方の企業様にて選定いただいている最中ですので、当選発表をお待ち下さい。
■ 選んだ理由

クライアント企業様から
「面白さという面では100%ではないが、熱を感じた。」
と評価いただきました。

■ 提案者全員のお礼・コメント

当選のご連絡が大変遅くなりまして申し訳ございませんでした。
クライアント企業様も、皆様から寄せられた案が秀逸で選定に相当悩んでおりましたが、この度決定いたしました。
多数採用したいところですが、苦渋の決断でした。
みなさま多数のご参加本当にありがとうございました。
この度選ばれなかった方も、機会がございましたらまたよろしくお願いいたします。

```html
<!DOCTYPE html>
<html lang="ja">
<head>
<meta charset="utf-8">
<title>SORANO INDUSTRY</title>
<link rel="stylesheet" href="https://fonts.googleapis.com/css2?family=Noto+Sans+JP:wght@400;500;700&family=Noto+Serif+JP:wght@400;600&family=Roboto+Condensed:wght@400;700&display=swap">
<style>
:root{
  --navy:#16365f;
  --navy-dark:#0f2447;
  --blue:#3b6aa0;
  --line:#c9d3de;
  --grey:#f1f3f5;
  --text:#333;
  --white:#fff;
}
*{box-sizing:border-box;margin:0;padding:0}
html,body{width:1200px;height:3692px;overflow:hidden}
body{font-family:"Noto Sans JP",sans-serif;color:var(--text);background:var(--white);position:relative}
.top{position:absolute;top:0;left:0;width:1200px}
.site-header{height:84px;display:flex;align-items:center;padding:0 40px;border-bottom:4px solid var(--navy)}
.brand{display:flex;align-items:center;gap:12px;width:320px}
.brand-mark{width:30px;height:30px;background:var(--navy)}
.brand-name{font-family:"Roboto Condensed",sans-serif;font-weight:700;font-size:26px;color:var(--navy);letter-spacing:1px;white-space:nowrap}
.global-nav{display:flex;flex:1;justify-content:space-between;padding-right:50px}
.global-nav a{color:var(--navy);text-decoration:none;font-size:18px;font-weight:500;white-space:nowrap}
.hero{height:516px;position:relative;background:linear-gradient(180deg,#9fb3c8 0%,#c9d4df 45%,#8a9aab 100%)}
.hero-photo{position:absolute;inset:0}
.hero-copy{position:absolute;left:600px;top:210px;font-family:"Roboto Condensed",sans-serif;font-weight:700;color:var(--white);font-size:38px;letter-spacing:6px;line-height:1.25;text-align:right}
.hero-rule{height:14px;background:linear-gradient(90deg,var(--navy),var(--blue),var(--navy))}
.news{margin:40px 40px 0;border:1px solid var(--line)}
.news h2{font-size:18px;font-weight:500;padding:10px 16px;border-bottom:1px solid var(--line);color:var(--navy)}
.news ul{list-style:none}
.news li{display:flex;gap:26px;padding:11px 16px;font-size:15px;border-bottom:1px solid var(--line);white-space:nowrap;overflow:hidden}
.news li:last-child{border-bottom:0}
.news time{flex:none}
.section-bar{margin:0 40px;height:46px;background:var(--navy);color:var(--white);font-size:21px;font-weight:700;display:flex;align-items:center;padding-left:20px;border-left:8px solid var(--blue)}
.greeting{position:absolute;top:980px;left:0;width:1200px}
.greeting-body{margin:10px 40px 0;height:360px;display:flex;align-items:center;background:var(--grey)}
.greeting-photo{width:560px;height:340px;margin-left:10px;background:linear-gradient(135deg,#2c3e55,#7d8da1 60%,#c3ccd6)}
.greeting-quote{margin-left:50px;font-family:"Noto Serif JP",serif;font-size:28px;line-height:1.7;color:#222}
.greeting-quote .sign{display:block;text-align:right}
.company{position:absolute;top:1448px;left:0;width:1200px}
.company-lead{margin:16px 40px 0;font-size:14px;white-space:nowrap}
.company-links{margin:20px 40px 0;display:flex;gap:20px}
.company-link{flex:1;height:212px;display:flex;align-items:center;justify-content:center;border:4px solid var(--navy)}
.company-link span{background:rgba(255,255,255,.85);padding:14px 70px;font-size:24px;letter-spacing:12px;color:var(--navy);font-weight:500}
.link-philosophy{background:linear-gradient(135deg,#6f8fb8,#d8e2ee)}
.link-history{background:linear-gradient(135deg,#a8b8c6,#e3e8ee)}
.products{position:absolute;top:1920px;left:0;width:1200px}
.products-body{margin:18px 40px 0;display:flex;gap:14px;height:550px}
.product-card{width:362px;border:1px solid var(--line);background:var(--white)}
.product-photo{height:240px;background:linear-gradient(180deg,#2e2e2e,#5a5a5a)}
.product-card h3{font-size:17px;font-weight:500;padding:14px 14px 8px;line-height:1.45;min-height:78px}
.product-card dl{padding:0 14px;font-size:15px;line-height:1.95}
.product-card dl div{border-bottom:1px solid var(--line)}
.product-note{flex:1;background:var(--navy-dark);color:var(--white);padding:32px 30px;font-size:20px;line-height:1.7}
.product-note p{margin-bottom:26px}
.recruit{position:absolute;top:2520px;left:0;width:1200px}
.recruit-banner{margin:18px 40px 0;height:268px;background:linear-gradient(90deg,#c5ccd4,#e8ebef 50%,#b7c0ca);display:flex;align-items:center;justify-content:center}
.recruit-banner p{font-family:"Noto Serif JP",serif;font-size:46px;color:var(--navy-dark);letter-spacing:8px;font-weight:600}
.contact{position:absolute;top:2872px;left:0;width:1200px}
.contact-body{margin:18px 40px 0;display:flex;gap:18px}
.office{width:350px}
.office-card{border:1px solid var(--line);height:230px;padding:18px 22px;font-size:16px;line-height:1.75}
.office-card h3{font-size:18px;font-weight:700;margin-bottom:4px}
.office-map{margin-top:16px;height:380px;background:linear-gradient(135deg,#e4ecd8,#f4f1e8 50%,#dfe7ef);border:1px solid var(--line)}
.mail-card{flex:1;border:1px solid var(--line);height:230px;display:flex;flex-direction:column;align-items:center;justify-content:center;font-size:16px;line-height:1.7}
.mail-card svg{margin-bottom:22px}
.site-footer{position:absolute;bottom:0;left:0;width:1200px;height:52px;background:var(--navy);color:var(--white);display:flex;align-items:center;justify-content:center;font-size:15px}
</style>
</head>
<body>
<div class="top">
  <header class="site-header">
    <div class="brand"><span class="brand-mark"></span><span class="brand-name">SORANO INDUSTRY</span></div>
    <nav class="global-nav">
      <a href="#greeting">ご挨拶</a><a href="#company">会社案内</a><a href="#products">製品案内</a><a href="#recruit">採用情報</a><a href="#contact">お問い合わせ</a>
    </nav>
  </header>
  <section class="hero">
    <div class="hero-photo" role="img" aria-label="手のひらに浮かぶ地球とネットワークのアイコン、都市の風景写真"></div>
    <p class="hero-copy">NO FUN<br>NO MANUFACTURE</p>
  </section>
  <div class="hero-rule"></div>
  <section class="news">
    <h2>NEWS</h2>
    <ul>
      <li><time>2018.01.15</time><span>新聞に当社の製品が紹介されました新聞に当社の製品が紹介されました新聞に当社の製品が紹介されました</span></li>
      <li><time>2018.02.21</time><span>新聞に当社の製品が紹介されました新聞に当社の製品が紹介されました新聞に当社の製品が紹介されました新聞に当社の製品が紹介されました</span></li>
      <li><time>2018.04.08</time><span>新聞に当社の製品が紹介されました</span></li>
      <li><time>2018.09.04</time><span>秋田県の課題企業に認定されました</span></li>
    </ul>
  </section>
</div>

<section class="greeting" id="greeting">
  <h2 class="section-bar">ご挨拶</h2>
  <div class="greeting-body">
    <div class="greeting-photo" role="img" aria-label="工場で作業する社員の後ろ姿の写真"></div>
    <p class="greeting-quote">「No Fun No Manufacture」<br>面白くなくっちゃ、<br>ものづくりじゃない<span class="sign">代表取締役　山田健一</span></p>
  </div>
</section>

<section class="company" id="company">
  <h2 class="section-bar">会社案内</h2>
  <p class="company-lead">当社は、1978年に東京都青葉市にて創業した極小径精密マイクロシャフト、小径円筒コロ、小径ニードルローラーを製造販売する会社です</p>
  <div class="company-links">
    <a class="company-link link-philosophy" role="img" aria-label="工場建物のイラストと経営理念へのリンク"><span>経営理念</span></a>
    <a class="company-link link-history" role="img" aria-label="社屋の写真と会社沿革へのリンク"><span>会社沿革</span></a>
  </div>
</section>

<section class="products" id="products">
  <h2 class="section-bar">製品案内</h2>
  <div class="products-body">
    <article class="product-card">
      <div class="product-photo" role="img" aria-label="クロスローラーと円筒コロの製品写真"></div>
      <h3>クロスローラー、円筒コロ</h3>
      <dl>
        <div>径：0.5μ〜　全長：L1.0mm〜</div>
        <div>注文単位：1本〜</div>
        <div>真円度：0.0003μm〜</div>
        <div>外径公差：0.001μm Lange〜</div>
      </dl>
    </article>
    <article class="product-card">
      <div class="product-photo" role="img" aria-label="モーターシャフトとピンゲージの製品写真"></div>
      <h3>モーターシャフト、偏芯軸<br>ガイドピン、ピンゲージ</h3>
      <dl>
        <div>径：0.35μ〜　全長：L1.0mm〜</div>
        <div>注文単位：1本〜</div>
        <div>真円度：0.0003μm〜</div>
        <div>外径公差：0.001μm Lange〜</div>
      </dl>
    </article>
    <div class="product-note">
      <p>小ロットに思いを込めて、精一杯対応させて頂きます。</p>
      <p>小ロットよりオーダーメイド可能です。</p>
      <p>納期はご相談に応じてご対応させて頂きます。</p>
      <p>海外からのお問合せ(英語)にもご対応させて頂きます。</p>
    </div>
  </div>
</section>

<section class="recruit" id="recruit">
  <h2 class="section-bar">採用情報</h2>
  <div class="recruit-banner" role="img" aria-label="社員たちの集合写真を背景にしたキャッチコピー">
    <p>すべてをかけて、打ちこめること</p>
  </div>
</section>

<section class="contact" id="contact">
  <h2 class="section-bar">お問い合わせ</h2>
  <div class="contact-body">
    <div class="office">
      <div class="office-card">
        <h3>東京本社</h3>
        〒190-0042<br>東京都青葉市緑ヶ丘3-18-7 2F<br>Tel: 042-555-0173<br>Fax: 042-555-0174
      </div>
      <div class="office-map" role="img" aria-label="東京本社周辺の地図"></div>
    </div>
    <div class="office">
      <div class="office-card">
        <h3>秋田工場</h3>
        〒018-0555<br>秋田県北川市若杉町2-41<br>Tel: 0187-55-0128<br>Fax: 0187-55-0129
      </div>
      <div class="office-map" role="img" aria-label="秋田工場周辺の地図"></div>
    </div>
    <div class="mail-card">
      <svg width="130" height="90" viewBox="0 0 130 90" aria-hidden="true"><rect x="3" y="3" width="124" height="84" fill="none" stroke="#16365f" stroke-width="5"/><polyline points="3,3 65,50 127,3" fill="none" stroke="#16365f" stroke-width="5"/></svg>
      <span>email：info@sorano-works.jp</span>
      <span>お気軽にお問合せ下さい。</span>
    </div>
  </div>
</section>

<footer class="site-footer">Copyright Sorano Industry 2018. All Rights Reserved.</footer>
</body>
</html>
```